Real Estate Agent needs business card design

We have logo designed already, want to have business card designed. Very interested in those smaller size business card as they look very trendy. Business name is called VORENDA REALTY

```html
<!DOCTYPE html>
<html lang="en">
<head>
<meta charset="utf-8">
<title>Vorenda Realty — Business Card</title>
<link rel="stylesheet" href="https://fonts.googleapis.com/css2?family=Cinzel:wght@500&family=Open+Sans:wght@400;600;700&display=swap">
<style>
  :root {
    --backdrop: #1e1e1f;
    --card-white: #f6f6f4;
    --card-dark-top: #3d3d3f;
    --card-dark-bottom: #2a2a2c;
    --gold: #c19a62;
    --ink: #2a2a2a;
    --paper-text: #f2f2f2;
    --muted-text: #d8d8d8;
    --divider: rgba(255, 255, 255, 0.35);
  }
  * { margin: 0; padding: 0; box-sizing: border-box; }
  html, body {
    width: 1200px;
    height: 900px;
    overflow: hidden;
    background: var(--backdrop);
  }
  .canvas {
    position: relative;
    width: 1200px;
    height: 900px;
  }
  .card {
    position: absolute;
    left: 240px;
    width: 720px;
    height: 400px;
    box-shadow: 0 18px 40px rgba(0, 0, 0, 0.45);
  }
  .card--front {
    top: 40px;
    background: var(--card-white);
    display: flex;
    align-items: center;
    justify-content: center;
  }
  .card--back {
    top: 460px;
    background: linear-gradient(160deg, var(--card-dark-top), var(--card-dark-bottom));
  }
  .brand {
    display: flex;
    flex-direction: column;
    align-items: center;
    gap: 22px;
  }
  .brand__mark {
    width: 46px;
    height: 46px;
    background: var(--gold);
  }
  .brand__name {
    font-family: "Cinzel", serif;
    font-weight: 500;
    font-size: 40px;
    letter-spacing: 1px;
    color: var(--ink);
    white-space: nowrap;
  }
  .card--back .brand {
    position: absolute;
    left: 40px;
    top: 150px;
    width: 330px;
  }
  .card--back .brand__mark { width: 38px; height: 38px; }
  .card--back .brand__name {
    font-size: 30px;
    color: var(--paper-text);
  }
  .divider {
    position: absolute;
    left: 392px;
    top: 64px;
    width: 1px;
    height: 272px;
    background: linear-gradient(to bottom, transparent, var(--divider) 20%, var(--divider) 80%, transparent);
  }
  .contact {
    position: absolute;
    left: 420px;
    top: 72px;
    font-family: "Open Sans", sans-serif;
    font-size: 15px;
    line-height: 1.45;
    color: var(--muted-text);
  }
  .contact__name {
    font-weight: 700;
    color: var(--gold);
    text-transform: uppercase;
    letter-spacing: 0.5px;
  }
  .contact__title {
    text-transform: uppercase;
    margin-bottom: 14px;
  }
  .contact__address { margin-bottom: 14px; }
  .contact__web {
    font-weight: 700;
    color: var(--paper-text);
    letter-spacing: 0.5px;
  }
</style>
</head>
<body>
  <main class="canvas">
    <section class="card card--front" aria-label="Card front">
      <div class="brand">
        <span class="brand__mark"></span>
        <span class="brand__name">VORENDA REALTY</span>
      </div>
    </section>

    <section class="card card--back" aria-label="Card back">
      <div class="brand">
        <span class="brand__mark"></span>
        <span class="brand__name">VORENDA REALTY</span>
      </div>
      <span class="divider"></span>
      <div class="contact">
        <p class="contact__name">Dana Hollis</p>
        <p class="contact__title">CEO/Founder</p>
        <p class="contact__address">4120 Alder Crest Way<br>Juneau, Alaska 99801</p>
        <p>P: 555 210 4837</p>
        <p>M: 555 318 6092</p>
        <p>F: 555 402 7715</p>
        <p>E: dana@vorendarealty.com</p>
        <p class="contact__web">www.vorendarealty.com</p>
      </div>
    </section>
  </main>
</body>
</html>
```